Factory Beam Works

We manufacture and distribute luminaires for industrial lighting applications. We cover the European market. We look for a basic well designed web site, with not too much text, as we're gonna do it multilingual. Requirements: a.) Wordpress Avada Theme b.) Pages: 1. Start (compare http://www.brivantel.co.kr/rb/?r=en and www.morvack.de for slides => mixed products & industry photos) 2. Company (short description) http://www.morvack.de/en/company/about-us, european map with offices in Stockholm (Sweden), Berlin Heidelberg (Germany), Linz (Austria) Description fill in : "The name of FBW stands for competence and quality in all areas of technical light fittings: waterproof / dustproof light fittings - industrial-grade light fittings - outdoor luminaires - A very high level of reliability, of competence and innovation their mark on thinking and actions of people working in the family company. FBW for a very long time: research and development, laboratory work, toolmaking, polyester pressing plant, sheet metal forming, powder coating and assembly are concentrated in FBW's own premises. Worldwide innovations have helped FBW over and over again to launch new impulses to the market. For decades now FBW has been one of the leading bidders of this industrial sector. The international significance of FBW as a lighting specialist is based on intelligent and useful solutions - not just with respect to standard products but as far as branch-specific technical problems or application conditions and particular customer wishes are concerned. "3. Products [pls. see infographic under https://www.quendora.com/en/applications/industry/lighting-for-industry/ [we are looking for something similar to start on top, then short description product with download pdf] 4. News (Events, new products, etc.) 5. Partner login (for downloads of further data, well structured) 6. Contact (4 office adresses, map, no contact form) c.) Logo / Colors: 1 Logo with 2 different colors, please choose either blue or red one or the colors according to your recommendation d.) What do we do? High quality industrial lighting smart lighting control e.) Industries: Look at this photo here for a glimpse: http://www.pelmarot-werk.de/lichttechnik f.) Areas: Look at the infographic here, to get an idea which areas of lighting / products we are covering: https://www.quendora.com/en/applications/industry/lighting-for-industry/ => Design / Associations: Fresh, clear, technology, high quality, solidity, reliability experience like https://www.quendora.com/en/applications/industry/lighting-for-industry/ Thank you very much for your offers!

Target Market(s)

Resellers / Wholesalers of industrial luminaires AND direct clients (industrial, commercial)

Industry/Entity Type

Light Industrial

Coding

Coded - Design and coding required

Number of Pages Required

5+ page

Font styles to use
Sans Serif

Colors
0355a3
ec1f27

Requirements
Must have
• a.) Wordpress Avada Theme b.) Pages: 1. Start / 2. Company (short description, european map with offices in Stockholm (Sweden), Berlin Heidelberg (Germany), Linz (Austria) / 3. Products [pls infographic under f.) => News (Events, new products, etc.) / 5. Partner Login (for Downloads) / 6. Contact c.) Logo / Colors: 1 Logo with 2 different colors, please choose either blue or red one or the colors according to your recommendation d.) What do we do? High quality industrial lighting smart lighting control e.) Industries: Look at this photo here for a glimpse: http://www.pelmarot-werk.de/lichttechnik f.) Areas: Look at the infographic here, to get an idea which areas of lighting / products we are covering: https: //www.quendora. com / en / applications / industry / lighting-for-industry / => Design / Associations: Fresh, clear, technology, high quality, solidity, reliability experience => tidy look
Nice to have
• - some nice WP Avada elements - map with locations (see b.) 2.) above) - infographic (see f.) above)
Should not have
• not too overloaded, not too crowded

```html
<!DOCTYPE html>
<html lang="en">
<head>
<meta charset="utf-8">
<title>Factory Beam Works</title>
<link rel="stylesheet" href="https://fonts.googleapis.com/css2?family=Orbitron:wght@700;900&family=Montserrat:wght@400;500;600;700&display=swap">
<style>
:root{
  --red:#ec1f27;
  --dark:#2b2b2b;
  --text:#4a4a4a;
  --muted:#6b6b6b;
  --white:#ffffff;
  --footer-bar:#333333;
  --display:'Orbitron', sans-serif;
  --body:'Montserrat', sans-serif;
}
*{margin:0;padding:0;box-sizing:border-box}
html,body{width:1200px;height:3666px;overflow:hidden}
body{position:relative;background:var(--white);font-family:var(--body);color:var(--text)}
section,header,footer{position:absolute;left:0;width:1200px}

/* header */
.site-header{top:0;height:110px;background:var(--white)}
.brand{position:absolute;left:52px;top:22px;display:flex;flex-direction:column;align-items:center}
.brand-name{font-family:var(--body);font-weight:700;color:var(--red);font-size:40px;letter-spacing:4px;line-height:1}
.brand-sub{font-family:var(--body);font-weight:700;color:var(--red);font-size:14px;letter-spacing:2px;margin-top:6px}
.main-nav{position:absolute;right:50px;top:44px;display:flex;gap:40px;font-size:15px;font-weight:500;color:var(--dark)}

/* hero */
.hero{top:110px;height:720px;overflow:hidden}
.hero-photo{position:absolute;inset:0;
  background:
    radial-gradient(ellipse 28% 45% at 50% 48%,rgba(235,240,245,.75) 0%,rgba(235,240,245,0) 100%),
    linear-gradient(90deg,#8f969c 0%,#b7bdc2 14%,#7d7a70 24%,rgba(120,130,140,0) 38%,rgba(120,130,140,0) 62%,#5d6f86 76%,#8a7f6c 88%,#a8adb2 100%),
    linear-gradient(180deg,#c9ced3 0%,#9fa6ad 22%,#8d939a 45%,#b8bcbf 70%,#d6d8da 100%)}
.hero-shade{position:absolute;inset:0;background:rgba(30,35,45,.28)}
.hero-title{position:absolute;left:0;right:0;top:270px;text-align:center;color:var(--white);font-family:var(--display);font-weight:700;letter-spacing:4px}
.hero-title .line1{font-size:38px;display:block}
.hero-title .line2{font-size:50px;display:block;margin-top:6px;font-weight:900}
.btn-outline-light{position:absolute;left:508px;top:402px;width:186px;height:46px;border:2px solid var(--white);color:var(--white);font-size:16px;font-weight:500;display:flex;align-items:center;justify-content:center;letter-spacing:1px}

/* section headings */
.section-heading{font-family:var(--display);font-weight:900;color:var(--red);font-size:44px;letter-spacing:4px}
.heading-rule{height:3px;background:var(--red);width:190px;margin-top:10px}

/* about */
.about{top:830px;height:520px}
.about-image{position:absolute;left:50px;top:0;width:440px;height:480px;
  background:
    linear-gradient(90deg,transparent 0,transparent 128px,#222 128px,#222 131px,transparent 131px),
    linear-gradient(90deg,transparent 0,transparent 324px,#222 324px,#222 327px,transparent 327px),
    radial-gradient(ellipse 26% 12% at 30% 82%,#111 0%,#2a2a2a 60%,rgba(42,42,42,0) 100%),
    radial-gradient(ellipse 22% 22% at 30% 62%,#9a9a9a 0%,#5a5a5a 55%,rgba(90,90,90,0) 100%),
    radial-gradient(ellipse 18% 9% at 75% 60%,#111 0%,#2a2a2a 60%,rgba(42,42,42,0) 100%),
    radial-gradient(ellipse 15% 15% at 75% 45%,#a0a0a0 0%,#5e5e5e 55%,rgba(94,94,94,0) 100%);
  background-size:100% 58%,100% 46%,100% 100%,100% 100%,100% 100%,100% 100%;
  background-repeat:no-repeat}
.about-copy{position:absolute;left:525px;top:68px;width:620px}
.about-copy p{font-size:14px;line-height:27px;margin-top:28px;color:var(--text)}
.btn-outline-red{display:inline-flex;align-items:center;justify-content:center;width:186px;height:44px;border:2px solid var(--red);color:var(--red);font-size:17px;font-weight:500;margin-top:16px}

/* who we are */
.who{top:1350px;height:455px;background:linear-gradient(180deg,#ec1f27 0%,#e81c24 100%);text-align:center;color:var(--white)}
.who .section-heading{color:var(--white);margin-top:80px}
.who .heading-rule{background:var(--white);margin:8px auto 0}
.who p{width:1000px;margin:20px auto 0;font-size:14px;line-height:30px}
.btn-outline-white{display:inline-flex;align-items:center;justify-content:center;width:186px;height:44px;border:2px solid var(--white);color:var(--white);font-size:17px;font-weight:500;margin-top:18px}

/* products */
.products{top:1805px;height:900px}
.products .section-heading{position:absolute;left:52px;top:75px}
.products .heading-rule{position:absolute;left:52px;top:140px;width:184px}
.product-grid{position:absolute;left:52px;top:200px;width:1096px;display:grid;grid-template-columns:repeat(3,1fr);column-gap:50px;row-gap:58px}
.product-card{display:flex;flex-direction:column}
.product-image{width:230px;height:190px;margin-left:40px}
.tone-black{background:radial-gradient(ellipse 38% 42% at 50% 58%,#e8ecef 0%,#5a5e62 30%,#2a2c2e 60%,rgba(42,44,46,0) 100%)}
.tone-silver{background:radial-gradient(ellipse 42% 22% at 50% 76%,#ffffff 0%,#e8e8e8 50%,rgba(230,230,230,0) 100%),radial-gradient(ellipse 26% 34% at 50% 40%,#8d8d8d 0%,#b9b9b9 55%,rgba(185,185,185,0) 100%)}
.tone-pendant{background:radial-gradient(ellipse 40% 20% at 50% 78%,#2a2a2a 0%,#555 55%,rgba(85,85,85,0) 100%),linear-gradient(90deg,transparent 38%,#9ea4a8 40%,#e2e5e7 50%,#9ea4a8 60%,transparent 62%);background-size:100% 100%,100% 70%;background-repeat:no-repeat}
.tone-linear{background:radial-gradient(ellipse 44% 20% at 50% 74%,#cfcfcf 0%,#7d7d7d 45%,rgba(125,125,125,0) 100%),radial-gradient(ellipse 26% 30% at 45% 42%,#6b6b6b 0%,#b5b5b5 55%,rgba(181,181,181,0) 100%)}
.tone-flood{background:radial-gradient(ellipse 48% 28% at 50% 62%,#0e0e0e 0%,#2b2b2b 55%,rgba(43,43,43,0) 100%),radial-gradient(ellipse 34% 10% at 50% 26%,#1a1a1a 0%,rgba(26,26,26,0) 100%)}
.product-name{font-size:22px;line-height:32px;color:var(--muted);margin-top:24px}

/* testimonials */
.testimonials{top:2705px;height:585px}
.testimonials-bg{position:absolute;inset:0;background:radial-gradient(ellipse at 50% 40%,#e6e6e6 0%,#d8d8d8 55%,#cacaca 100%)}
.testimonials .section-heading{position:absolute;left:0;right:0;top:85px;text-align:center}
.testimonials .heading-rule{position:absolute;left:505px;top:150px;width:190px}
.avatar{position:absolute;left:493px;top:170px;width:190px;height:190px;border-radius:50%;border:6px solid var(--white);
  background:
    radial-gradient(ellipse 30% 20% at 50% 100%,#1c1c1c 0%,#1c1c1c 80%,rgba(28,28,28,0) 100%),
    radial-gradient(ellipse 55% 30% at 50% 98%,#2a2a2a 0%,#2a2a2a 70%,rgba(42,42,42,0) 100%),
    radial-gradient(ellipse 26% 36% at 50% 42%,#e9c3a6 0%,#d7a888 50%,rgba(140,100,70,0) 100%),
    radial-gradient(ellipse 36% 46% at 50% 44%,#8a6a4c 0%,#b08c66 60%,rgba(176,140,102,0) 100%),
    linear-gradient(180deg,#f6f6f6,#e4e4e4)}
.quote-badge{position:absolute;left:630px;top:296px;width:50px;height:50px;border-radius:50%;background:var(--red);color:var(--white);font-size:40px;font-weight:700;line-height:62px;text-align:center;font-family:Georgia,serif}
.client-name{position:absolute;left:0;right:0;top:370px;text-align:center;color:var(--red);font-size:21px;font-weight:600}
.testimonial-text{position:absolute;left:210px;width:780px;top:420px;text-align:center;font-size:14px;line-height:27px;color:var(--text)}

/* footer */
.site-footer{top:3290px;height:310px;background:var(--white)}
.footer-brand{position:absolute;left:52px;top:80px;width:294px;display:flex;flex-direction:column;align-items:center}
.footer-brand .brand-name{font-size:52px}
.footer-brand .brand-sub{font-size:16px;border-top:2px solid var(--red);padding-top:6px}
.social-list{position:absolute;left:60px;top:200px;display:flex;gap:16px}
.social-list span{width:30px;height:30px;border-radius:50%;background:var(--red)}
.footer-col h3{font-size:19px;font-weight:600;color:var(--red);margin-bottom:16px}
.contact-col{position:absolute;left:508px;top:74px}
.contact-col p{font-size:14px;line-height:31px;color:var(--text)}
.newsletter-col{position:absolute;left:802px;top:74px;width:346px}
.newsletter-col p{font-size:14px;line-height:22px}
.subscribe-form{display:flex;margin-top:18px;height:42px}
.subscribe-input{flex:1;border:2px solid var(--red);border-right:none;display:flex;align-items:center;padding-left:22px;font-size:14px;color:var(--muted)}
.subscribe-btn{width:116px;background:var(--red);color:var(--white);font-weight:700;font-size:15px;display:flex;align-items:center;justify-content:center}
.footer-bar{top:3600px;height:66px;background:var(--footer-bar);color:var(--white);font-size:15px;font-weight:600;display:flex;align-items:center;justify-content:center;letter-spacing:.5px}
</style>
</head>
<body>

<header class="site-header">
  <div class="brand"><span class="brand-name">FBW</span><span class="brand-sub">FACTORY BEAM WORKS</span></div>
  <nav class="main-nav"><span>Home</span><span>Company</span><span>Products</span><span>News</span><span>Partner</span><span>Contact</span></nav>
</header>

<section class="hero">
  <div class="hero-photo" role="img" aria-label="Photo of a large warehouse interior with tall shelving and industrial ceiling lights"></div>
  <div class="hero-shade"></div>
  <h1 class="hero-title"><span class="line1">FBW STANDS FOR</span><span class="line2">COMPETENCE AND QUALITY</span></h1>
  <span class="btn-outline-light">EXPLORE</span>
</section>

<section class="about">
  <div class="about-image" role="img" aria-label="Two black industrial high-bay luminaires hanging from cables"></div>
  <div class="about-copy">
    <h2 class="section-heading">ABOUT US</h2>
    <div class="heading-rule"></div>
    <p>Lorem ipsum dolor sit amet, consectetur adipiscing elit, sed do eiusmod tempor incididunt ut labore et dolore magna aliqua. Ut enim ad minim veniam, quis nostrud exercitation ullamco laboris nisi ut aliquip ex ea commodo consequat. Duis aute irure dolor in reprehenderit in voluptate velit esse cillum dolore eu fugiat nulla pariatur. Excepteur sint occaecat cupidatat non proident.</p>
    <span class="btn-outline-red">Know More</span>
  </div>
</section>

<section class="who">
  <h2 class="section-heading">WHO WE ARE</h2>
  <div class="heading-rule"></div>
  <p>Lorem ipsum dolor sit amet, consectetur adipiscing elit, sed do eiusmod tempor incididunt ut labore et dolore magna aliqua. Ut enim ad minim veniam, quis nostrud exercitation ullamco laboris nisi ut aliquip ex ea commodo consequat. Duis aute irure dolor in reprehenderit in voluptate velit esse cillum dolore eu fugiat nulla pariatur. Excepteur sint occaecat cupidatat non proident.</p>
  <span class="btn-outline-white">Know More</span>
</section>

<section class="products">
  <h2 class="section-heading">PRODUCTS</h2>
  <div class="heading-rule"></div>
  <div class="product-grid">
    <div class="product-card"><div class="product-image tone-black" role="img" aria-label="Black round LED flood luminaire with bracket"></div><p class="product-name">Sed ut perspiciatis unde omnis iste natus volm.</p></div>
    <div class="product-card"><div class="product-image tone-silver" role="img" aria-label="Silver high-bay luminaire with white reflector"></div><p class="product-name">Sed ut perspiciatis unde omnis iste natus volm.</p></div>
    <div class="product-card"><div class="product-image tone-pendant" role="img" aria-label="Cylindrical pendant luminaire with black shade"></div><p class="product-name">Sed ut perspiciatis unde omnis iste natus volm.</p></div>
    <div class="product-card"><div class="product-image tone-linear" role="img" aria-label="Linear high-bay LED luminaire with metal housing"></div><p class="product-name">Sed ut perspiciatis unde omnis iste natus volm.</p></div>
    <div class="product-card"><div class="product-image tone-flood" role="img" aria-label="Black rectangular LED flood light panel"></div><p class="product-name">Sed ut perspiciatis unde omnis iste natus volm.</p></div>
    <div class="product-card"><div class="product-image tone-silver" role="img" aria-label="Silver high-bay luminaire with white reflector"></div><p class="product-name">Sed ut perspiciatis unde omnis iste natus volm.</p></div>
  </div>
</section>

<section class="testimonials">
  <div class="testimonials-bg" role="img" aria-label="Light grey background with faint line drawings of hanging lamps"></div>
  <h2 class="section-heading">TESTIMONIALS</h2>
  <div class="heading-rule"></div>
  <div class="avatar" role="img" aria-label="Portrait photo of the client"></div>
  <div class="quote-badge">&ldquo;</div>
  <p class="client-name">Miss.Hanna Verlo</p>
  <p class="testimonial-text">Sed ut perspiciatis unde omnis iste natus error sit voluptatem accusantium doloremque laudantium, totam rem aperiam, eaque ipsa quae ab illo inventore veritatis et quasi architecto beatae vitae dicta sunt explicabo. Nemo enim ipsam voluptatem quia voluptas.</p>
</section>

<footer class="site-footer">
  <div class="footer-brand"><span class="brand-name">FBW</span><span class="brand-sub">FACTORY BEAM WORKS</span></div>
  <div class="social-list"><span></span><span></span><span></span><span></span><span></span><span></span></div>
  <div class="footer-col contact-col">
    <h3>Contact</h3>
    <p>418 Harbor Ridge Ave</p>
    <p>Suite 204</p>
    <p>(800) 000-0000</p>
    <p>Fax (800) 000-000</p>
    <p>Email:info@FBW.com</p>
  </div>
  <div class="footer-col newsletter-col">
    <h3>Newsletter</h3>
    <p>Enter your email address to get the latest University news, special events and student activities delivered.</p>
    <div class="subscribe-form"><span class="subscribe-input">Your Email-Id</span><span class="subscribe-btn">Subscribe</span></div>
  </div>
</footer>

<footer class="footer-bar">FBW © 2017 All Rights Reserved | Privacy Policy</footer>

</body>
</html>
```